Bright Harbor website redesign

We need a redesign for a website: mybrightharbor.com.

I already created a video going over what exactly is needed in the design.

See Video here: https://files.vortexa-share.com/file/d/7kPqLm2Xz9RtYw4Nb8Vc3Hd5Jf6Gs1Aa0/view?usp=sharing

Vortexa Deck shown in Video: https://decks.vortexa-share.com/presentation/d/9QwErTy7UiOpAsDfGhJkLzXcVbNm2Qw3ErTy4UiOpAs/edit?usp=sharing
Updates

Holidays in India so we did not get enough design entries or quality.

Target Market(s)

Dentistry

Industry/Entity Type

Dentistry

Number of Pages Required

1 page

Colors
0094D4
00A9DD
6FCCEA
C7EBF8
E9F6FB
00AB8E
00BBA5
67D7C9
C6EFE9
E9F9F6

Requirements
Must have
• See 13 min video link in description - shows what to do.

```html
<!DOCTYPE html>
<html lang="en">
<head>
<meta charset="utf-8">
<title>Bright Harbor – Dental Care</title>
<link href="https://fonts.googleapis.com/css2?family=Poppins:wght@400;500;600;700;800&display=swap" rel="stylesheet">
<style>
:root{
  --blue-deep:#0094d4;
  --blue:#00a9dd;
  --blue-soft:#6fccea;
  --blue-pale:#c7ebf8;
  --blue-mist:#e9f6fb;
  --teal-deep:#00ab8e;
  --teal:#00bba5;
  --teal-soft:#67d7c9;
  --teal-pale:#c6efe9;
  --teal-mist:#e9f9f6;
  --ink:#1f4f66;
  --text:#3b4a54;
  --muted:#5e6b73;
  --white:#ffffff;
}
*{box-sizing:border-box;margin:0;padding:0}
html,body{width:1200px;height:3940px;overflow:hidden;background:var(--white)}
body{position:relative;font-family:'Poppins',sans-serif;color:var(--text)}
.abs{position:absolute}
/* header */
.locations-tab{left:520px;top:0;width:172px;height:44px;background:var(--ink);border-radius:0 0 40px 40px;color:#fff;font-size:11px;font-weight:600;text-align:center;line-height:38px}
.brand{left:90px;top:34px;font-size:34px;font-weight:500;color:var(--teal-deep);letter-spacing:1px}
.brand-dot{display:inline-block;width:14px;height:14px;border-radius:50%;background:var(--blue);margin-left:8px;vertical-align:middle}
.phone{left:112px;top:114px;font-size:21px;font-weight:600;color:var(--ink)}
.btn{display:inline-block;border-radius:22px;color:#fff;font-weight:600;text-align:center}
.btn-schedule{left:848px;top:60px;width:152px;height:32px;line-height:32px;font-size:11px;background:var(--teal-deep)}
.btn-emergency{left:1005px;top:60px;width:106px;height:32px;line-height:32px;font-size:11px;background:var(--blue-deep)}
.nav{left:352px;top:118px;display:flex;gap:29px;font-size:12px;font-weight:500;color:var(--text)}
/* hero */
.hero{left:0;top:170px;width:1200px;height:620px}
.hero-title{left:114px;top:286px;font-size:66px;font-weight:800;line-height:62px;color:#fff}
.hero-sub{left:115px;top:490px;font-size:14px;font-weight:500;color:#fff}
.btn-hero{left:115px;top:533px;width:200px;height:42px;line-height:42px;font-size:12px;background:#fff;color:var(--ink)}
.hero-art{left:560px;top:236px;width:530px;height:510px;border-radius:50%;background:radial-gradient(circle at 55% 45%,rgba(255,255,255,.95) 0%,rgba(233,246,251,.8) 38%,rgba(199,235,248,.35) 58%,rgba(199,235,248,0) 70%)}
/* team */
.section-title{width:1200px;left:0;text-align:center;font-size:40px;font-weight:600;color:var(--ink)}
.arrow{font-size:26px;color:var(--blue);font-weight:600}
.member{width:214px;height:214px;border-radius:50%;background:linear-gradient(180deg,var(--blue-mist),var(--blue-pale))}
.member.dim{opacity:.55}
.member-name{left:0;width:1200px;text-align:center}
.link-detail{left:0;width:1200px;text-align:center;top:1238px;font-size:12px;font-weight:600;color:var(--teal-deep);text-decoration:underline}
.divider{left:90px;top:1345px;width:1020px;height:1px;background:#dedede}
/* services */
.service{width:200px;text-align:center}
.service svg{display:block;margin:0 auto}
.service-name{margin-top:14px;font-size:18px;font-weight:500;color:var(--text)}
/* review */
.review-bg{left:0;top:1690px;width:1200px;height:676px}
.review-title{left:170px;top:2000px;font-size:70px;font-weight:800;line-height:70px;color:#fff}
.review-sub{left:172px;top:2176px;font-size:25px;font-weight:600;color:#fff}
.card{left:650px;top:1797px;width:372px;height:506px;background:#fff;border-radius:24px}
.card-inner{left:65px;top:200px;width:253px;height:260px;background:var(--teal-mist);border-radius:10px}
.avatar{width:54px;height:54px;border-radius:50%;background:linear-gradient(135deg,#b89478,#6f5a4c)}
/* experience */
.exp-photo{left:75px;top:2450px;width:485px;height:600px;border-radius:220px 220px 0 0;background:linear-gradient(180deg,#6a4a3a 0%,#c99a7c 30%,#49c6e3 55%,#27b4d6 85%,#5d7fa0 100%)}
.exp-title{left:628px;top:2452px;font-size:42px;font-weight:600;line-height:49px;color:var(--ink)}
.exp-body{left:630px;top:2577px;width:482px;font-size:13.3px;line-height:19.6px;color:var(--muted)}
.exp-body p{margin-bottom:18px}
/* commitment */
.commit{left:0;top:3020px;width:1200px;height:508px}
.commit-title{left:0;width:1200px;top:3236px;text-align:center;font-size:42px;font-weight:600;line-height:46px;color:#fff}
.commit-sub{left:0;width:1200px;top:3344px;text-align:center;font-size:18px;font-weight:500;color:#fff}
.btn-commit{left:501px;top:3390px;width:198px;height:42px;line-height:42px;font-size:12px;background:var(--teal)}
/* footer */
.foot-head{font-size:14px;font-weight:600;color:var(--ink)}
.foot-text{font-size:12.5px;line-height:19px;color:var(--muted)}
.map{left:513px;top:3650px;width:273px;height:140px;background:linear-gradient(135deg,var(--blue-mist),var(--blue-pale));border:2px solid var(--blue-pale)}
.btn-foot{left:163px;top:3762px;width:254px;height:42px;line-height:42px;font-size:12px;background:var(--teal-deep)}
.hours{left:876px;top:3652px;font-size:12.5px;line-height:22px;color:var(--muted);border-collapse:collapse}
.hours td{padding:0;width:97px}
.foot-line{left:90px;top:3888px;width:1020px;height:1px;background:#e2e2e2}
.copyright{left:163px;top:3905px;font-size:12px;color:var(--muted)}
.social{width:24px;height:24px;border-radius:50%}
.to-top{left:1130px;top:3855px;width:48px;height:48px;border-radius:50%;background:var(--ink);color:#fff;text-align:center;line-height:46px;font-size:20px}
</style>
</head>
<body>

<!-- Header -->
<div class="abs locations-tab">VIEW LOCATIONS</div>
<div class="abs brand">Bright Harbor<span class="brand-dot"></span></div>
<div class="abs phone">(555) 014-2290</div>
<a class="abs btn btn-schedule">SCHEDULE ONLINE</a>
<a class="abs btn btn-emergency">EMERGENCY</a>
<nav class="abs nav">
  <span>ABOUT US ˅</span><span>SERVICES ˅</span><span>FINANCING</span><span>TESTIMONIALS</span><span>NEW PATIENT VISIT</span><span>SPECIALS</span><span>CONTACT US</span><span>BLOG</span>
</nav>

<!-- Hero -->
<svg class="abs hero" viewBox="0 0 1200 620" preserveAspectRatio="none">
  <defs>
    <linearGradient id="heroGrad" x1="0" y1="0" x2="1" y2="1">
      <stop offset="0" stop-color="#00a9dd"/>
      <stop offset="1" stop-color="#0094d4"/>
    </linearGradient>
  </defs>
  <path d="M0 0H1200V300C900 490 450 700 0 500Z" fill="var(--blue-pale)"/>
  <path d="M0 0H1200V285C900 470 450 675 0 485Z" fill="url(#heroGrad)"/>
</svg>
<div class="abs hero-art" role="img" aria-label="Three glossy white and translucent teeth illustration"></div>
<h1 class="abs hero-title">CREATING<br>HEALTHIER<br>SMILES</h1>
<div class="abs hero-sub">With Advanced Technology and Affordable Treatment</div>
<a class="abs btn btn-hero">BOOK AN APPOINTMENT</a>

<!-- Team -->
<h2 class="abs section-title" style="top:834px">Meet Our Team</h2>
<div class="abs arrow" style="left:166px;top:1002px">‹</div>
<div class="abs arrow" style="left:1020px;top:1002px">›</div>
<div class="abs member dim" style="left:233px;top:913px" role="img" aria-label="Portrait of a team member"></div>
<div class="abs member" style="left:493px;top:913px" role="img" aria-label="Portrait of Dr. Anika Sharma"></div>
<div class="abs member dim" style="left:753px;top:913px" role="img" aria-label="Portrait of a team member"></div>
<div class="abs member-name" style="top:1150px;font-size:18px;font-weight:500;color:var(--ink)">Dr. Anika Sharma</div>
<div class="abs member-name" style="top:1177px;font-size:11.5px;font-weight:500">Endodontist</div>
<div class="abs member-name" style="top:1198px;font-size:11.5px;font-weight:500">DDS</div>
<a class="abs link-detail">DOCTOR'S DETAILED INFORMATION</a>
<div class="abs divider"></div>

<!-- Services -->
<h2 class="abs section-title" style="top:1400px">Our Services</h2>
<div class="abs arrow" style="left:166px;top:1520px">‹</div>
<div class="abs arrow" style="left:1020px;top:1520px">›</div>
<div class="abs service" style="left:223px;top:1476px">
  <svg width="124" height="124" viewBox="0 0 124 124"><circle cx="62" cy="62" r="60" fill="none" stroke="var(--teal-deep)" stroke-width="2"/><path d="M46 36c8-6 24-6 32 0c2 10-4 16-16 16s-18-6-16-16zM56 54h12l-2 36h-8z" fill="none" stroke="var(--teal-deep)" stroke-width="2"/></svg>
  <div class="service-name">Dental Implants</div>
</div>
<div class="abs service" style="left:422px;top:1476px">
  <svg width="124" height="124" viewBox="0 0 124 124"><circle cx="62" cy="62" r="60" fill="none" stroke="var(--teal-deep)" stroke-width="2"/><path d="M40 42c6-10 20-8 22-2c2-6 16-8 22 2c4 12-4 22-6 42c-2 6-8 6-9 0l-3-16c-2-4-6-4-8 0l-3 16c-1 6-7 6-9 0c-2-20-10-30-6-42z" fill="none" stroke="var(--teal-deep)" stroke-width="2"/><rect x="48" y="48" width="28" height="10" fill="none" stroke="var(--teal-deep)" stroke-width="2"/></svg>
  <div class="service-name">Braces</div>
</div>
<div class="abs service" style="left:616px;top:1476px">
  <svg width="124" height="124" viewBox="0 0 124 124"><circle cx="62" cy="62" r="60" fill="none" stroke="var(--teal-deep)" stroke-width="2"/><path d="M52 54c6-10 18-8 20-2c2-6 14-8 18 2c4 10-4 18-6 34c-2 6-6 6-7 0l-3-12c-2-3-4-3-6 0l-3 12c-1 6-5 6-7 0c-2-16-10-24-6-34z" fill="none" stroke="var(--teal-deep)" stroke-width="2"/><circle cx="44" cy="44" r="5" fill="none" stroke="var(--teal-deep)" stroke-width="2"/><circle cx="56" cy="36" r="4" fill="none" stroke="var(--teal-deep)" stroke-width="2"/></svg>
  <div class="service-name">Cosmetic Dentistry</div>
</div>
<div class="abs service" style="left:813px;top:1476px">
  <svg width="124" height="124" viewBox="0 0 124 124"><circle cx="62" cy="62" r="60" fill="none" stroke="var(--teal-deep)" stroke-width="2"/><path d="M38 44c6-12 20-10 24-4c4-6 18-8 24 4c4 14-4 24-8 40c-2 6-6 6-8 0l-4-14c-2-4-6-4-8 0l-4 14c-2 6-6 6-8 0c-4-16-12-26-8-40z" fill="none" stroke="var(--teal-deep)" stroke-width="2"/></svg>
  <div class="service-name">Crowns</div>
</div>

<!-- Reviews -->
<svg class="abs review-bg" viewBox="0 0 1200 676" preserveAspectRatio="none">
  <defs>
    <linearGradient id="reviewGrad" x1="0" y1="0" x2="1" y2="1">
      <stop offset="0" stop-color="#00bba5"/>
      <stop offset="1" stop-color="#00ab8e"/>
    </linearGradient>
  </defs>
  <path d="M0 300C350 80 800 -30 1200 40V676H0Z" fill="var(--teal-pale)"/>
  <path d="M0 318C350 110 800 0 1200 62V676H0Z" fill="url(#reviewGrad)"/>
</svg>
<div class="abs" style="left:278px;top:1768px;width:248px;height:186px;border-radius:0 0 124px 124px;background:rgba(255,255,255,.18)"></div>
<h2 class="abs review-title">Review<br>Widget</h2>
<div class="abs review-sub">What Our Patients Say About Us</div>

<div class="abs card">
  <div class="abs" style="left:0;width:372px;top:20px;text-align:center;font-size:15px;font-weight:500;color:var(--ink)">Average Rating</div>
  <svg class="abs" style="left:100px;top:50px" width="140" height="26" viewBox="0 0 140 26">
    <g fill="#f5b81c">
      <path d="M12 1l3.4 7 7.6 1-5.5 5.3 1.3 7.6L12 18.3 5.2 21.9l1.3-7.6L1 9l7.6-1z"/>
      <path transform="translate(27 0)" d="M12 1l3.4 7 7.6 1-5.5 5.3 1.3 7.6L12 18.3 5.2 21.9l1.3-7.6L1 9l7.6-1z"/>
      <path transform="translate(54 0)" d="M12 1l3.4 7 7.6 1-5.5 5.3 1.3 7.6L12 18.3 5.2 21.9l1.3-7.6L1 9l7.6-1z"/>
      <path transform="translate(81 0)" d="M12 1l3.4 7 7.6 1-5.5 5.3 1.3 7.6L12 18.3 5.2 21.9l1.3-7.6L1 9l7.6-1z"/>
      <path transform="translate(108 0)" d="M12 1l3.4 7 7.6 1-5.5 5.3 1.3 7.6L12 18.3 5.2 21.9l1.3-7.6L1 9l7.6-1z" opacity=".45"/>
    </g>
  </svg>
  <div class="abs" style="left:241px;top:51px;font-size:17px;font-weight:600;color:var(--ink)">4.9</div>
  <div class="abs" style="left:133px;top:88px;width:20px;height:20px;border-radius:50%;background:var(--blue)"></div>
  <div class="abs" style="left:160px;top:89px;font-size:11px;font-weight:500">238 Reviews</div>
  <div class="abs" style="left:40px;top:130px;width:292px;height:1px;background:#e5e5e5"></div>
  <div class="abs" style="left:44px;top:148px;font-size:16px;font-weight:600;color:var(--ink)">Searchly</div>
  <div class="abs" style="left:148px;top:148px;font-size:16px;font-weight:600;color:var(--ink)">Ratewise</div>
  <div class="abs" style="left:246px;top:148px;font-size:16px;font-weight:600;color:var(--ink)">Friendbook</div>
  <div class="abs arrow" style="left:18px;top:312px;font-size:22px">‹</div>
  <div class="abs arrow" style="left:340px;top:312px;font-size:22px">›</div>
  <div class="abs card-inner">
    <div class="abs avatar" style="left:10px;top:16px" role="img" aria-label="Reviewer profile photo"></div>
    <div class="abs" style="left:72px;top:18px;font-size:12px;letter-spacing:1px;color:#f5b81c">★★★★★</div>
    <div class="abs" style="left:72px;top:36px;font-size:15px;font-weight:600;color:var(--ink)">Marisa K.</div>
    <div class="abs" style="left:10px;top:86px;width:236px;font-size:11px;line-height:17.5px;color:var(--muted)">I am so happy I found Bright Harbor in Lakeview. This is a long over due review since I have been seeing them for almost two years... <span style="color:var(--blue)">more</span></div>
    <div class="abs" style="left:10px;top:165px;font-size:11px;font-weight:500;color:var(--ink)">26 February, 2021</div>
    <div class="abs" style="left:0;top:210px;width:253px;height:1px;background:#d9ece8"></div>
    <div class="abs" style="left:10px;top:230px;font-size:11.5px;color:var(--muted)">Source:</div>
    <div class="abs" style="left:178px;top:228px;font-size:15px;font-weight:600;color:var(--ink)">Ratewise</div>
  </div>
</div>

<!-- Experience -->
<div class="abs exp-photo" role="img" aria-label="Smiling young woman in a turquoise sweater pointing at herself"></div>
<h2 class="abs exp-title">Experience the Bright<br>Harbor Difference</h2>
<div class="abs exp-body">
  <p>Your smile is our #1 priority. At Bright Harbor, we provide affordable and expert dental solutions. Whether you are looking for a family dentist or have any emergency such as needing a root canal in Lakeview, we are here for you! We want to keep your teeth healthy inside and out. We don't just clean teeth and send you on your way, we want to get to know you.</p>
  <p>We accept most HMO and PPO insurances. We offer various financing options through CarePay, LendBridge and In-House Plans.</p>
  <p>To constantly strive to achieve the highest level of skills and modern techniques and equipment so we can provide our patients with the best that Dentistry has to offer at our dental office in Lakeview, Bay County, CA.</p>
  <p>We provide patients with the best experience you can find in all of the Coastal Region. We provide a comfortable and friendly atmosphere to shatter any fears you may have. We supply you with all the information on your dental health options so you can feel comfortable in the choices you make, whether it's a routine check-up or dental implants in Lakeview.</p>
  <p>We are available for Emergency and Walk-ins.</p>
</div>

<!-- Commitment -->
<svg class="abs commit" viewBox="0 0 1200 508" preserveAspectRatio="none" role="img" aria-label="Faded photo of a patient smiling in the dental chair">
  <defs>
    <linearGradient id="commitGrad" x1="0" y1="0" x2="1" y2="0">
      <stop offset="0" stop-color="#0b5f86"/>
      <stop offset=".55" stop-color="#0094d4"/>
      <stop offset="1" stop-color="#00a9dd"/>
    </linearGradient>
  </defs>
  <path d="M0 110C380 -20 800 -20 1200 30V508H0Z" fill="var(--blue-pale)"/>
  <path d="M0 132C380 0 800 0 1200 52V508H0Z" fill="url(#commitGrad)"/>
</svg>
<h2 class="abs commit-title">Committed to excellence in<br>Oral Health Care</h2>
<div class="abs commit-sub">Free Exam and X-Rays for New Patients</div>
<a class="abs btn btn-commit">BOOK AN APPOINTMENT</a>

<!-- Footer -->
<div class="abs foot-head" style="left:163px;top:3614px">BRIGHT HARBOR</div>
<div class="abs foot-text" style="left:163px;top:3648px">482 Maple Crest Ave., Suite B<br>Lakeview, CA 90000</div>
<div class="abs foot-text" style="left:163px;top:3697px">Call Us: (555) 014-2290</div>
<div class="abs foot-text" style="left:163px;top:3729px">hello@mybrightharbor.com</div>
<a class="abs btn btn-foot">BOOK YOUR FREE CONSULTATION</a>

<div class="abs foot-head" style="left:513px;top:3614px">MAP &amp; DIRECTIONS</div>
<div class="abs map" role="img" aria-label="Street map showing the office location"></div>

<div class="abs foot-head" style="left:876px;top:3614px">OFFICE HOURS:</div>
<table class="abs hours">
  <tr><td>Monday</td><td>10AM–7PM</td></tr>
  <tr><td>Tuesday</td><td>10AM–7PM</td></tr>
  <tr><td>Wednesday</td><td>9AM–6PM</td></tr>
  <tr><td>Thursday</td><td>9AM–6PM</td></tr>
  <tr><td>Friday</td><td>9AM–5PM</td></tr>
  <tr><td>Saturday</td><td>9AM–1PM</td></tr>
</table>

<div class="abs foot-line"></div>
<div class="abs copyright">All rights reserved. MyBrightHarbor.com | Disclaimer &amp; Terms | Privacy Policy | Sitemap</div>
<div class="abs social" style="left:931px;top:3900px;background:var(--blue-deep)"></div>
<div class="abs social" style="left:962px;top:3900px;background:var(--blue)"></div>
<div class="abs social" style="left:993px;top:3900px;background:var(--teal-deep)"></div>
<div class="abs social" style="left:1024px;top:3900px;background:var(--teal)"></div>
<div class="abs to-top">↑</div>

</body>
</html>
```